Design business cards for Ironvale Barbers (Opening March so won't need finalised till January2018

Ironvale Barbers is the new age barbers and skincare for all men. Creating tailor made haircuts & customised skincare solutions for the perfect healthy manly look. The Barbers will have a industrial, rustic, worldly feel about it. Rustic red brick wall with old wine barrels as the work stations with the old fashion barber chairs. Concrete floor and a bit corrugated iron around.
Target Market(s)
Professional males who like a great haircut, wet shave and may consider a facial if in the right environment. Total pampering experience in a boys environment.
Industry/Entity Type
Barber
Contact Information for Business Card
Front- Logo - address is 42 Kowhai Rd Taupo
Ph - (07) 548 9163
www.ironvalebarbers.com
email - hello@ironvale.co.nz
Back of card
Mens Haircare - Wet Shaving - Facials - Skin Prescriptions
We are doing a loyalty program - 6 squares numbered then 7th free
Colors
Designer to choose colors to be used in the design.
Requirements
Must have
- Clean simple easy to read.
Nice to have
- Our current colours are white font on black background but thinking we need to introduce another colour. Maybe white logo on a copper, bronze or rusty background. Or even a rustic red brick wall with white writing. Want it clean simple to read. Maybe a burgundy?
Should not have
- no images like heads, scissors, razors please

```html
<!DOCTYPE html>
<html lang="en">
<head>
<meta charset="utf-8">
<title>Ironvale Barbers – Business Card</title>
<link href="https://fonts.googleapis.com/css2?family=Roboto+Slab:wght@400;700&display=swap" rel="stylesheet">
<style>
  :root {
    --backdrop: #2a2a2a;
    --card-black: #1c1b1b;
    --card-edge: #b89a3e;
    --ink-white: #e9e7e3;
    --accent-gold: #b8953f;
    --divider: #6e5a2a;
  }
  * { margin: 0; padding: 0; box-sizing: border-box; }
  html, body {
    width: 1200px;
    height: 720px;
    overflow: hidden;
    background: var(--backdrop);
  }
  .stage {
    width: 1200px;
    height: 720px;
    display: flex;
    align-items: center;
    justify-content: center;
  }
  .business-card {
    position: relative;
    width: 900px;
    height: 550px;
    background: var(--card-black);
    border-bottom: 3px solid var(--card-edge);
    border-left: 3px solid var(--card-edge);
    box-shadow: 0 30px 60px rgba(0, 0, 0, 0.55);
  }
  .brand-name {
    position: absolute;
    left: 90px;
    top: 190px;
    width: 340px;
    text-align: center;
    font-family: "Roboto Slab", serif;
    font-weight: 700;
    color: var(--ink-white);
    text-transform: uppercase;
    line-height: 1;
  }
  .brand-name .brand-main {
    display: block;
    font-size: 60px;
    letter-spacing: 1px;
  }
  .brand-name .brand-sub {
    display: block;
    margin-top: 14px;
    font-size: 22px;
    letter-spacing: 9px;
  }
  .card-divider {
    position: absolute;
    left: 470px;
    top: 90px;
    width: 1px;
    height: 330px;
    background: var(--divider);
  }
  .contact-list {
    position: absolute;
    left: 500px;
    top: 150px;
    list-style: none;
    font-family: "Roboto Slab", serif;
    font-weight: 400;
    font-size: 19px;
    color: var(--ink-white);
  }
  .contact-item {
    display: flex;
    align-items: center;
    gap: 12px;
    height: 30px;
  }
  .contact-icon {
    width: 16px;
    height: 16px;
    flex: none;
    fill: none;
    stroke: var(--accent-gold);
    stroke-width: 1.6;
  }
  .contact-icon .solid { fill: var(--accent-gold); stroke: none; }
</style>
</head>
<body>
<main class="stage">
  <section class="business-card" aria-label="Ironvale Barbers business card front">
    <h1 class="brand-name">
      <span class="brand-main">Ironvale</span>
      <span class="brand-sub">Barbers</span>
    </h1>

    <div class="card-divider"></div>

    <ul class="contact-list">
      <li class="contact-item">
        <svg class="contact-icon" viewBox="0 0 16 16" aria-hidden="true">
          <path class="solid" d="M4 1.5 6 4.5 4.8 6c.8 2 2.3 3.5 4.2 4.3L10.5 9l3 2-1 2.5c-.3.6-1 .9-1.6.7C6.3 12.8 3.2 9.7 1.8 5.1c-.2-.6.1-1.3.7-1.6Z"/>
        </svg>
        <span>Phone Number</span>
      </li>
      <li class="contact-item">
        <svg class="contact-icon" viewBox="0 0 16 16" aria-hidden="true">
          <rect x="1.5" y="3.5" width="13" height="9"/>
          <path d="M1.5 3.5 8 9l6.5-5.5"/>
        </svg>
        <span>www.ironvalebarbers.com</span>
      </li>
      <li class="contact-item">
        <svg class="contact-icon" viewBox="0 0 16 16" aria-hidden="true">
          <circle cx="8" cy="8" r="6.5"/>
          <ellipse cx="8" cy="8" rx="2.8" ry="6.5"/>
          <path d="M1.5 8h13"/>
        </svg>
        <span>hello@ironvale.co.nz</span>
      </li>
      <li class="contact-item">
        <svg class="contact-icon" viewBox="0 0 16 16" aria-hidden="true">
          <path class="solid" d="M8 1a5 5 0 0 0-5 5c0 3.6 5 9 5 9s5-5.4 5-9a5 5 0 0 0-5-5Zm0 7a2 2 0 1 1 0-4 2 2 0 0 1 0 4Z"/>
        </svg>
        <span>42 Kowhai Rd Taupo</span>
      </li>
    </ul>
  </section>
</main>
</body>
</html>
```